Tall Cedar Builders Business Card

I'm looking for a business card design for a start-up Handyman/Construction Company. The organization will double as a ministry to the homeless, hoping to create job opportunity and training to the homeless, providing a pathway back to being "homed". I'm looking for a simple to "seeming" simple design. Open to all thoughts.

Industry/Entity Type

Ministry

Requirements
Must have
• Logo (Attached), Name, Phone, Email and Address. Note - "*Registered and Insured".

```html
<!DOCTYPE html>
<html lang="en">
<head>
<meta charset="utf-8">
<title>Tall Cedar Builders Business Card</title>
<link rel="stylesheet" href="https://fonts.googleapis.com/css2?family=Delius&display=swap">
<style>
  :root {
    --backdrop: #2b2b2d;
    --card: #f7f7f8;
    --navy: #2c3654;
    --purple: #7b2a8c;
    --card-shadow: rgba(0, 0, 0, 0.45);
  }
  * { box-sizing: border-box; margin: 0; padding: 0; }
  html, body {
    width: 1200px;
    height: 900px;
    overflow: hidden;
    background: var(--backdrop);
    font-family: "Delius", "Comic Sans MS", cursive;
  }
  .canvas {
    position: relative;
    width: 1200px;
    height: 900px;
  }
  .card {
    position: absolute;
    width: 560px;
    height: 320px;
    background: var(--card);
    box-shadow: 0 18px 40px var(--card-shadow);
  }
  .card--front { left: 60px; top: 110px; }
  .card--back { left: 580px; top: 470px; }

  /* Front */
  .brand {
    position: absolute;
    inset: 0;
    display: flex;
    align-items: center;
    justify-content: center;
    gap: 14px;
  }
  .brand__mark {
    width: 22px;
    height: 22px;
    background: var(--purple);
  }
  .brand__name {
    font-size: 44px;
    color: var(--navy);
    letter-spacing: 1px;
  }

  /* Back */
  .identity {
    position: absolute;
    top: 40px;
    left: 0;
    right: 0;
    text-align: center;
  }
  .identity__name {
    font-size: 38px;
    color: var(--navy);
    letter-spacing: 2px;
    line-height: 1;
  }
  .identity__role {
    font-size: 20px;
    color: var(--purple);
    margin-top: 4px;
    letter-spacing: 0.5px;
  }
  .contact {
    position: absolute;
    top: 138px;
    left: 196px;
    list-style: none;
  }
  .contact__item {
    display: flex;
    align-items: center;
    gap: 10px;
    font-size: 14px;
    color: var(--navy);
    height: 21px;
  }
  .contact__icon { width: 14px; height: 14px; fill: var(--purple); }
  .credential {
    position: absolute;
    left: 0;
    right: 0;
    bottom: 36px;
    display: flex;
    align-items: center;
    justify-content: center;
    gap: 16px;
  }
  .credential__band {
    width: 96px;
    height: 14px;
    background: var(--purple);
  }
  .credential__text {
    font-size: 26px;
    color: var(--navy);
    letter-spacing: 0.5px;
  }
</style>
</head>
<body>
<main class="canvas">
  <section class="card card--front" aria-label="Card front">
    <div class="brand">
      <span class="brand__mark"></span>
      <span class="brand__name">Tall Cedar Builders</span>
    </div>
  </section>

  <section class="card card--back" aria-label="Card back">
    <header class="identity">
      <h1 class="identity__name">YOUR NAME</h1>
      <p class="identity__role">Company Position</p>
    </header>
    <ul class="contact">
      <li class="contact__item">
        <svg class="contact__icon" viewBox="0 0 16 16" aria-hidden="true"><path d="M8 1 1 7.5h2V15h4v-4h2v4h4V7.5h2z"/></svg>
        Your Address
      </li>
      <li class="contact__item">
        <svg class="contact__icon" viewBox="0 0 16 16" aria-hidden="true"><path d="M1 6c0-2 3-3.5 7-3.5S15 4 15 6v1.5h-3.5V6h-7v1.5H1zM3.5 8.5h9L14 14H2z"/></svg>
        000 123 456
      </li>
      <li class="contact__item">
        <svg class="contact__icon" viewBox="0 0 16 16" aria-hidden="true"><path d="M1 3h14v10H1zm1.5 1.5v.3L8 9l5.5-4.2v-.3zm0 2.2v4.8h11V6.7L8 11z"/></svg>
        youremail@domain.com
      </li>
    </ul>
    <div class="credential">
      <span class="credential__band"></span>
      <span class="credential__text">Registered and Insured</span>
      <span class="credential__band"></span>
    </div>
  </section>
</main>
</body>
</html>
```